Very professional Urgent Care TRI FOLD brochure

We need a TRI FOLD brochure design to be super professional to our urgent care center. We are high quality urgent care located in Chicago, IL. The feel of the brochure MUST be very professional and brings quality to the reader. Medical Images MUST not be old and used before and uniqueness in professionalism is the key for the brochure. Please, get my wordings form the file brochure 2. the brochure might be white color with matching color from our logo such as the blue one

Target Market(s)

18 years old and above.

Industry/Entity Type

Medical

Colors
ffffff

Requirements
Must have
• Very high quality images

```html
<!DOCTYPE html>
<html lang="en">
<head>
<meta charset="utf-8">
<title>Summit Urgent Care – Tri-Fold Brochure</title>
<link rel="stylesheet" href="https://fonts.googleapis.com/css2?family=Tinos:wght@400;700&family=Arimo:wght@400;700&display=swap">
<style>
  :root {
    --brand-blue: #0f3ca5;
    --brand-red: #b5001f;
    --ink: #1f1f1f;
    --body-ink: #2b2b2b;
    --table-line: #c9c9c9;
    --table-fill: #f4f4f4;
    --tick-blue: #1b55b8;
    --photo-light: #eef3f8;
    --photo-mid: #c9d8e6;
  }
  * { box-sizing: border-box; margin: 0; padding: 0; }
  html, body { width: 1200px; height: 927px; overflow: hidden; background: #ffffff; }
  .brochure { position: relative; width: 1200px; height: 927px; background: #ffffff; font-family: "Arimo", Arial, sans-serif; color: var(--body-ink); }

  .photo { position: absolute; top: 0; width: 400px; height: 212px; }
  .photo--care-icons { left: 0; background: linear-gradient(180deg, #dce8f2 0%, #e9f0f7 60%, #ffffff 100%); }
  .photo--physician { left: 400px; background: linear-gradient(180deg, #e6edf4 0%, #f1f4f8 60%, #ffffff 100%); }
  .photo--stethoscope { left: 800px; background: linear-gradient(180deg, #d9dfe4 0%, #eceff2 60%, #ffffff 100%); }

  .serif-heading { font-family: "Tinos", "Times New Roman", serif; font-weight: 700; color: var(--ink); font-size: 20.5px; line-height: 24px; }

  .services { position: absolute; left: 34px; top: 214px; width: 340px; }
  .services__intro { margin-top: 22px; font-size: 14.4px; line-height: 16.5px; color: var(--ink); }
  .services__list { list-style: none; margin-top: 4px; padding-left: 19px; }
  .services__list li { position: relative; padding-left: 18px; font-size: 14.4px; line-height: 23px; color: var(--ink); }
  .services__list li::before { content: ""; position: absolute; left: 0; top: 8px; width: 7px; height: 7px; background: var(--brand-red); }
  .services__list li:nth-child(even)::before { background: var(--brand-blue); }

  .compare { position: absolute; left: 416px; top: 214px; border-collapse: collapse; width: 369px; }
  .compare td, .compare th { border: 1px solid var(--table-line); background: var(--table-fill); }
  .compare th { height: 52px; font-size: 10px; font-weight: 700; color: #111; line-height: 12px; }
  .compare td { height: 38.4px; font-size: 11.5px; color: var(--ink); line-height: 13.5px; }
  .compare .label { width: 171px; padding-left: 11px; text-align: left; }
  .compare .mark { width: 127px; text-align: center; }
  .compare .mark--er { width: 71px; }
  .compare th.blank { background: #ffffff; }
  .brand-name { font-family: "Tinos", "Times New Roman", serif; font-weight: 700; font-size: 12.5px; color: var(--brand-red); display: inline-flex; align-items: center; gap: 5px; }
  .brand-name .dot { width: 9px; height: 9px; border-radius: 50%; background: var(--brand-blue); }
  .icon { width: 18px; height: 18px; vertical-align: middle; }

  .notice { position: absolute; left: 400px; width: 400px; text-align: center; font-family: "Tinos", "Times New Roman", serif; font-size: 21px; line-height: 29px; }
  .notice--emergency { top: 641px; color: var(--brand-red); }
  .notice--onsite { top: 728px; color: var(--brand-blue); }

  .faq { position: absolute; left: 818px; width: 348px; }
  .faq h2 { letter-spacing: 0.2px; }
  .faq p { margin-top: 1px; font-size: 13.8px; line-height: 20.5px; text-align: justify; color: var(--body-ink); }
  .faq--when { top: 212px; }
  .faq--when h2 { line-height: 29px; }
  .faq--same { top: 506px; }
  .faq--charge { top: 680px; }
  .faq--charge h2 { line-height: 28px; }
  .faq--charge p { text-align: left; }

  .band { position: absolute; top: 838px; height: 89px; width: 400px; }
  .band--left { left: 0; background: var(--brand-blue); }
  .band--center { left: 400px; background: var(--brand-red); }
  .band--right { left: 800px; background: var(--brand-blue); }
</style>
</head>
<body>
<svg width="0" height="0" style="position:absolute">
  <defs>
    <symbol id="tick" viewBox="0 0 20 20">
      <circle cx="10" cy="10" r="8" fill="none" stroke="var(--tick-blue)" stroke-width="1.6"/>
      <path d="M5.5 10.2 L9 13.5 L17 4" fill="none" stroke="var(--tick-blue)" stroke-width="2" stroke-linecap="round" stroke-linejoin="round"/>
    </symbol>
    <symbol id="cross" viewBox="0 0 20 20">
      <circle cx="10" cy="10" r="8" fill="none" stroke="var(--brand-red)" stroke-width="1.6"/>
      <path d="M7 7 L13 13 M13 7 L7 13" stroke="var(--brand-red)" stroke-width="2.2" stroke-linecap="round"/>
    </symbol>
  </defs>
</svg>

<main class="brochure">
  <div class="photo photo--care-icons" role="img" aria-label="Photo of a clinician's hand with a stethoscope touching glowing medical icons"></div>
  <div class="photo photo--physician" role="img" aria-label="Photo of a smiling physician in a white coat using a tablet"></div>
  <div class="photo photo--stethoscope" role="img" aria-label="Photo of a stethoscope and pen resting on medical paperwork"></div>

  <section class="services">
    <h1 class="serif-heading">Comprehensive care for non-life threatening illness and injury</h1>
    <p class="services__intro">Walk in to Summit Urgent Care for quality treatments, including:</p>
    <ul class="services__list">
      <li>Allergic reactions</li>
      <li>Neck/Back Pain</li>
      <li>Gastroenteritis, stomach pain</li>
      <li>Vomiting, dehydration</li>
      <li>Kidney stones, renal colic</li>
      <li>Asthma, bronchitis, pneumonia</li>
      <li>Cuts, burns, bites</li>
      <li>Sprains, strains, broken bones</li>
      <li>Cold, Cough, Flu</li>
      <li>Minor eye injuries</li>
      <li>Rashes and other Skin condition</li>
      <li>Infections</li>
      <li>Aches and pains</li>
      <li>IV fluid,&nbsp; IV Medications</li>
      <li>Routine Check-Ups</li>
      <li>Immunization and vaccination</li>
      <li>EKG's, X-ray, laboratory services</li>
      <li>DOT testing</li>
      <li>School, camp, sports, work physicals</li>
      <li>Occupational&nbsp; health</li>
      <li>Most Illness and injuries</li>
      <li>And more....</li>
    </ul>
  </section>

  <table class="compare">
    <tr>
      <th class="blank"></th>
      <th class="mark"><span class="brand-name">Summit Urgent Care<span class="dot"></span></span></th>
      <th class="mark mark--er">Emergency<br>Room</th>
    </tr>
    <tr><td class="label">Board Certified Physicians</td><td class="mark"><svg class="icon"><use href="#tick"/></svg></td><td class="mark mark--er"><svg class="icon"><use href="#tick"/></svg></td></tr>
    <tr><td class="label">Extended Hours</td><td class="mark"><svg class="icon"><use href="#tick"/></svg></td><td class="mark mark--er"><svg class="icon"><use href="#tick"/></svg></td></tr>
    <tr><td class="label">minimal Wait Time</td><td class="mark"><svg class="icon"><use href="#tick"/></svg></td><td class="mark mark--er"><svg class="icon"><use href="#cross"/></svg></td></tr>
    <tr><td class="label">Effective Cost</td><td class="mark"><svg class="icon"><use href="#tick"/></svg></td><td class="mark mark--er"><svg class="icon"><use href="#cross"/></svg></td></tr>
    <tr><td class="label">Personal Attention</td><td class="mark"><svg class="icon"><use href="#tick"/></svg></td><td class="mark mark--er"><svg class="icon"><use href="#cross"/></svg></td></tr>
    <tr><td class="label">Easy Center Navigation</td><td class="mark"><svg class="icon"><use href="#tick"/></svg></td><td class="mark mark--er"><svg class="icon"><use href="#cross"/></svg></td></tr>
    <tr><td class="label">Treats Non-Life Threatening Illness and Injuries</td><td class="mark"><svg class="icon"><use href="#tick"/></svg></td><td class="mark mark--er"><svg class="icon"><use href="#tick"/></svg></td></tr>
    <tr><td class="label">Treats Life Threatening Illness and Injuries</td><td class="mark"><svg class="icon"><use href="#cross"/></svg></td><td class="mark mark--er"><svg class="icon"><use href="#tick"/></svg></td></tr>
  </table>

  <p class="notice notice--emergency">Dial 911 immediately for any medical<br>problem that seems life-threatening</p>
  <p class="notice notice--onsite">X-Rays, Lab and EKG Services On Site</p>

  <section class="faq faq--when">
    <h2 class="serif-heading">When Would I Go to an Urgent Care Center?</h2>
    <p>An urgent care center offers you convenience and affordability compared to an emergency room's long wait and high cost. This is the right choice when you need a medical provider for non-life threatening illnesses and injuries but you do not have an appointment. You could also visit an urgent care facility when your regular physician is on vacation, closed on nights and weekends or unable to offer you a timely appointment to address your medical concern.</p>
  </section>

  <section class="faq faq--same">
    <h2 class="serif-heading">Are All Urgent Care Centers the Same?</h2>
    <p>Not all urgent care facilities provide the same level of treatment. At Summit Urgent Care, we deliver advanced medical treatments you cannot find at a regular urgent care center. Summit Urgent Care also offers lower costs for care than a hospital-affiliated urgent care center or a trip to the ER.</p>
  </section>

  <section class="faq faq--charge">
    <h2 class="serif-heading">Does Summit Urgent Care Charge as an ER or Urgent Care Center?</h2>
    <p>We charge as an urgent care center while providing advanced treatment similar to an ER. Our cost is a fraction of what you would pay for a trip to the ER and close to the cost of a regular office visit.</p>
  </section>

  <div class="band band--left"></div>
  <div class="band band--center"></div>
  <div class="band band--right"></div>
</main>
</body>
</html>
```